Letterhead Design for Corvane Communications

We are a Telecommunications Company, We wanting to get our Letterhead sorted as the one we have now looks Dull, It be used across our different databases we use but also mainly in Word , I have attached our Logo for you also, our website is corvane-example.com.au

We would only like to show our postal Address which is PO Box 8142 Tilford Cove NSW 2497

and we need to show our ABN Number Which we would be ABN: 61 804 327 918

Target Market(s)

Looks Stunning for our Proposals and General Usage

Industry/Entity Type

Telecommunications

Requirements
Must have
• Our Postal Address Only and Our ABN Number
Should not have
• Not listing our Actual Address

```html
<!DOCTYPE html>
<html lang="en">
<head>
<meta charset="utf-8">
<title>Corvane Communications Letterhead</title>
<link rel="stylesheet" href="https://fonts.googleapis.com/css2?family=Open+Sans:wght@400;600&family=Roboto:wght@400&display=swap">
<style>
  :root {
    --backdrop: #dedede;
    --paper: #f8f8f8;
    --brand-orange: #e0581f;
    --brand-green: #1e8c3a;
    --body-text: #5a5a5a;
    --footer-text: #3c3c3c;
    --divider: #b9b9b9;
  }
  * { margin: 0; padding: 0; box-sizing: border-box; }
  html, body {
    width: 1153px; height: 1200px; overflow: hidden;
    background: var(--backdrop);
  }
  .letterhead {
    position: absolute; left: 170px; top: 35px;
    width: 812px; height: 1130px;
    background: var(--paper);
    box-shadow: 0 6px 22px rgba(0,0,0,0.14);
  }
  .brand {
    position: absolute; top: 82px; left: 0; right: 0;
    display: flex; align-items: center; justify-content: center; gap: 10px;
  }
  .brand-dot {
    width: 22px; height: 22px; border-radius: 50%;
    background: var(--brand-orange);
  }
  .brand-name {
    font-family: "Open Sans", sans-serif; font-weight: 600;
    font-size: 24px; letter-spacing: 1px;
    color: var(--brand-orange);
  }
  .letter-body {
    position: absolute; left: 80px; right: 81px; top: 278px;
    font-family: "Open Sans", sans-serif; font-size: 14.1px;
    line-height: 21.4px; color: var(--body-text);
  }
  .letter-body p { margin-bottom: 21.4px; text-align: justify; }
  .letter-body .salutation, .letter-body .closing { text-align: left; }
  .signature {
    position: absolute; left: 82px; top: 842px;
    width: 92px; height: 86px;
    background: linear-gradient(135deg, rgba(27,35,64,0.10), rgba(27,35,64,0.04));
  }
  .contact {
    position: absolute; left: 0; right: 0; top: 1034px;
    font-family: "Roboto", sans-serif; font-size: 16.5px;
    color: var(--footer-text); text-align: center; line-height: 22px;
  }
  .contact-line { display: flex; justify-content: center; align-items: center; gap: 6px; }
  .contact-divider { color: var(--divider); margin: 0 6px; }
  .contact-item { display: inline-flex; align-items: center; gap: 6px; margin: 0 2px; }
  .contact-item svg { fill: var(--brand-green); }
</style>
</head>
<body>
  <main class="letterhead">
    <header class="brand">
      <span class="brand-dot"></span>
      <span class="brand-name">Corvane Communications</span>
    </header>

    <section class="letter-body">
      <p class="salutation">Dear customer,</p>
      <p>Lorem ipsum dolor sit amet, consectetur adipisicing elit, sed do eiusmod tempor incididunt ut labore et dolore magna aliqua. Ut enim ad minim veniam, quis nostrud exercitation ullamco laboris nisi ut aliquip ex ea commodo consequat. Duis aute irure dolor in reprehenderit in voluptate velit esse cillum dolore eu fugiat nulla pariatur. Excepteur sint occaecat cupidatat non proident, sunt in culpa qui officia deserunt mollit anim id est laborum.</p>
      <p>Lorem ipsum dolor sit amet, consectetur adipisicing elit, sed do eiusmod tempor incididunt ut labore et dolore magna aliqua. Ut enim ad minim veniam, quis nostrud exercitation ullamco laboris nisi ut aliquip ex ea commodo consequat. Duis aute irure dolor in reprehenderit in voluptate velit esse cillum dolore eu fugiat nulla pariatur. Excepteur sint occaecat cupidatat non proident, sunt in culpa qui officia deserunt mollit anim id est laborum.</p>
      <p>Lorem ipsum dolor sit amet, consectetur adipisicing elit, sed do eiusmod tempor incididunt ut labore et dolore magna aliqua. Ut enim ad minim veniam, quis nostrud exercitation ullamco laboris nisi ut aliquip ex ea commodo consequat. Duis aute irure dolor in reprehenderit in voluptate velit esse cillum dolore eu fugiat nulla pariatur. Excepteur sint occaecat cupidatat non proident, sunt in culpa qui officia deserunt mollit anim id est laborum.</p>
      <p>Lorem ipsum dolor sit amet, consectetur adipisicing elit, sed do eiusmod tempor incididunt ut labore et dolore magna aliqua. Ut enim ad minim veniam, quis nostrud exercitation ullamco laboris nisi ut aliquip ex ea commodo consequat. Duis aute irure dolor in reprehenderit.</p>
      <p class="closing">Yours Sincerely,</p>
    </section>

    <div class="signature" role="img" aria-label="Handwritten signature"></div>

    <footer class="contact">
      <div class="contact-line">
        <span class="postal">PO Box 8142 Tilford Cove NSW 2497</span>
        <span class="contact-divider">|</span>
        <span class="abn">ABN: 61 804 327 918</span>
      </div>
      <div class="contact-line">
        <span class="contact-item">
          <svg width="14" height="13" viewBox="0 0 14 13" aria-hidden="true"><path d="M1 4c0-2 3-3 6-3s6 1 6 3v1h-3V4H4v1H1z"/><path d="M3 6h8l2 6H1z"/><circle cx="7" cy="9" r="1.6" fill="#f8f8f8"/></svg>
          1800 472 106
        </span>
        <span class="contact-item">
          <svg width="15" height="11" viewBox="0 0 15 11" aria-hidden="true"><path d="M0 0h15v2L7.5 6 0 2z"/><path d="M0 3.5l7.5 4 7.5-4V11H0z"/></svg>
          info@corvane-example.com.au
        </span>
        <span class="contact-item">
          <svg width="14" height="14" viewBox="0 0 14 14" aria-hidden="true"><circle cx="7" cy="7" r="7"/><path d="M4 3c2 0 3 1 2 3s-2 1-2 3M9 8c1 0 2 1 1 3" stroke="#f8f8f8" stroke-width="1.4" fill="none"/></svg>
          www.corvane-example.com.au
        </span>
      </div>
    </footer>
  </main>
</body>
</html>
```